Business Card Design.

Life and Wellness Coach
www.brightpathwell.com
Want to use my name as the logo it could be the initials TRH or my full name. I want to trade mark me.
I like clean lines and simple designs, but it pops using the colors scheme (one or two colors) on the website.
I provide life and health coaching virtually and in person. My services include: Nutrition Response Testing, Allergy Elimination Testing, Wellness Coaching, Life Coaching. Life and Health Assessments, and I sell foundational health products and specialized nutrition. Use colors that represent healing and trust.
Target Market(s)
Women for the ages of 30 - 60
Industry/Entity Type
Health
Contact Information for Business Card
Tessa Ravenna Holloway
Life and Wellness Coach
tessa@coachtrh.com
www.brightpathwell.com
443-781-6392
Health is not an event it's a lifestyle (tag line or if you have a better tag line)

```html
<!DOCTYPE html>
<html lang="en">
<head>
<meta charset="utf-8">
<title>Tessa Ravenna Holloway – Business Card</title>
<link rel="stylesheet" href="https://fonts.googleapis.com/css2?family=Pinyon+Script&family=Lato:wght@400;700&display=swap">
<style>
  :root {
    --stage: #232323;
    --berry: #9c1f4e;
    --berry-deep: #7e1440;
    --card: #f7f7f7;
    --card-shade: #e4e4e4;
    --ink: #2b2b2b;
    --photo-hair: #5a2f28;
    --photo-skin: #d9b7a2;
    --photo-sky: #aab8d4;
  }
  * { box-sizing: border-box; margin: 0; padding: 0; }
  html, body { width: 1200px; height: 873px; overflow: hidden; }
  body { background: var(--stage); font-family: "Lato", sans-serif; position: relative; }

  .card {
    position: absolute;
    background: linear-gradient(135deg, #ffffff 0%, var(--card) 55%, var(--card-shade) 100%);
    border: 6px solid var(--berry);
    border-radius: 26px;
    overflow: hidden;
  }

  /* Front */
  .card--front { left: 90px; top: 148px; width: 330px; height: 578px; }
  .portrait {
    position: absolute; inset: 0 0 130px 0;
    background:
      radial-gradient(ellipse 45% 40% at 45% 40%, var(--photo-skin) 0%, rgba(217,183,162,0) 100%),
      radial-gradient(ellipse 70% 60% at 30% 35%, var(--photo-hair) 0%, rgba(90,47,40,0) 100%),
      linear-gradient(160deg, #f2f2f2 0%, var(--photo-sky) 70%, #e9e9ef 100%);
    -webkit-mask-image: linear-gradient(to bottom, #000 50%, transparent 100%);
    mask-image: linear-gradient(to bottom, #000 50%, transparent 100%);
  }
  .card--front .signature { position: absolute; left: 18px; right: 18px; bottom: 42px; }
  .card--front .signature__name { font-size: 27px; }
  .card--front .signature__role { font-size: 13px; }

  /* Shared signature block */
  .signature { text-align: center; }
  .signature__name {
    font-family: "Pinyon Script", cursive;
    color: var(--berry);
    font-size: 34px;
    line-height: 1.1;
    white-space: nowrap;
  }
  .signature__name sup { font-family: "Lato", sans-serif; font-size: 9px; color: var(--ink); vertical-align: top; margin-left: 1px; }
  .signature__role {
    display: flex; align-items: center; justify-content: center; gap: 8px;
    margin-top: 6px;
    font-weight: 700; font-size: 14px; color: var(--ink);
  }
  .signature__role::before, .signature__role::after {
    content: ""; height: 2px; background: var(--berry); flex: 1;
  }

  /* Back */
  .card--back { left: 460px; top: 272px; width: 660px; height: 378px; }
  .card--back .signature { position: absolute; left: 60px; top: 38px; width: 380px; }
  .card--back .signature__name { font-size: 40px; }
  .card--back .signature__role { font-size: 16px; }

  .services { position: absolute; right: 36px; top: 150px; text-align: right; list-style: none; }
  .services__title {
    color: var(--berry); font-weight: 700; font-size: 15px;
    text-decoration: underline; margin-bottom: 8px; margin-right: 14px;
  }
  .services__item { font-size: 15px; color: var(--ink); line-height: 27px; }
  .services__item::after {
    content: ""; display: inline-block; width: 5px; height: 5px; border-radius: 50%;
    background: var(--berry); margin-left: 9px; vertical-align: middle;
  }

  .contact { position: absolute; left: 40px; bottom: 30px; list-style: none; }
  .contact li {
    display: flex; align-items: center; gap: 12px;
    font-weight: 700; font-size: 15px; color: var(--ink); line-height: 30px;
  }
  .contact svg { width: 17px; height: 17px; fill: none; stroke: var(--ink); stroke-width: 2; }
</style>
</head>
<body>

  <section class="card card--front">
    <div class="portrait" role="img" aria-label="Portrait photograph of the coach, smiling"></div>
    <div class="signature">
      <div class="signature__name">Tessa Ravenna Holloway<sup>®</sup></div>
      <div class="signature__role">Life and Wellness Coach</div>
    </div>
  </section>

  <section class="card card--back">
    <div class="signature">
      <div class="signature__name">Tessa Ravenna Holloway<sup>®</sup></div>
      <div class="signature__role">Life and Wellness Coach</div>
    </div>

    <ul class="services">
      <li class="services__title">MY SERVICES</li>
      <li class="services__item">Life Coaching</li>
      <li class="services__item">Wellness Coaching</li>
      <li class="services__item">Nutrition Response Testing</li>
      <li class="services__item">Allergy Elimination Testing</li>
      <li class="services__item">Life &amp; Health Assessments</li>
    </ul>

    <ul class="contact">
      <li>
        <svg viewBox="0 0 18 18" aria-hidden="true"><rect x="4" y="1.5" width="10" height="15" rx="1.5"/></svg>
        443-781-6392
      </li>
      <li>
        <svg viewBox="0 0 18 18" aria-hidden="true"><rect x="1.5" y="3.5" width="15" height="11" style="fill:var(--ink)"/><path d="M1.5 3.5 L9 10 L16.5 3.5" style="stroke:#fff"/></svg>
        tessa@coachtrh.com
      </li>
      <li>
        <svg viewBox="0 0 18 18" aria-hidden="true"><path d="M7.5 10.5 L10.5 7.5"/><path d="M8 5 L10 3 a3 3 0 0 1 5 5 L13 10"/><path d="M10 13 L8 15 a3 3 0 0 1 -5 -5 L5 8"/></svg>
        www.brightpathwell.com
      </li>
    </ul>
  </section>

</body>
</html>
```